Boarding Pass for Tour Company

We need an A6 sized boarding pass desinged for our tour company.

Colours to follow company logo. Image background with white text on top.

Require a strip at the bottom with text on top. This will be a group indicator colour. Can use purple for design.

Font styles to use
Sans Serif

Colors
0054AA
0677BA
7BADD7
CADEEF
E8F1F8

```html
<!DOCTYPE html>
<html lang="en">
<head>
<meta charset="utf-8">
<title>Skyward Ballooning – Boarding Pass</title>
<link rel="stylesheet" href="https://fonts.googleapis.com/css2?family=Montserrat:wght@700;800&family=Oswald:wght@600&display=swap">
<style>
  :root {
    --page: #ffffff;
    --card: #ffffff;
    --card-edge: #e2e6ea;
    --brand-blue: #29a6e0;
    --sky-top: #e9cf86;
    --sky-mid: #c9c79a;
    --hills: #8fa27c;
    --vines: #5f8a3e;
    --vines-deep: #486f2c;
    --text-light: #ffffff;
  }
  * { box-sizing: border-box; margin: 0; padding: 0; }
  html, body {
    width: 1200px; height: 1200px; overflow: hidden;
    background: var(--page);
  }
  .canvas { position: relative; width: 1200px; height: 1200px; }
  .pass {
    position: absolute; top: 324px;
    width: 390px; height: 550px;
    border-radius: 29px; overflow: hidden;
    background: var(--card);
    box-shadow: 0 0 0 1px var(--card-edge);
  }
  .pass--textured { left: 170px; }
  .pass--clean { left: 638px; }
  .pass__art { position: absolute; inset: 0; width: 390px; height: 550px; }
  .pass__brand {
    position: absolute; top: 34px; left: 0; width: 100%;
    text-align: center; color: var(--brand-blue);
    font-family: "Montserrat", sans-serif; font-weight: 800;
    line-height: 1;
  }
  .pass__brand-name { display: block; font-size: 34px; letter-spacing: 1px; }
  .pass__brand-sub { display: block; font-size: 17px; margin-top: 20px; }
  .pass__title {
    position: absolute; top: 274px; left: 0; width: 100%;
    text-align: center; color: var(--text-light);
    font-family: "Oswald", sans-serif; font-weight: 600;
    font-size: 50px; line-height: 50px; letter-spacing: 0.5px;
    text-transform: uppercase;
  }
  .pass__tag {
    position: absolute; top: 431px; left: 30px;
    color: var(--text-light);
    font-family: "Montserrat", sans-serif; font-weight: 700; font-size: 18px;
  }
  .pass__pilot {
    position: absolute; top: 483px; left: 0; width: 100%;
    text-align: center; color: var(--text-light);
    font-family: "Montserrat", sans-serif; font-weight: 700;
    font-size: 19px; letter-spacing: 2px; word-spacing: 6px;
  }
</style>
</head>
<body>
<main class="canvas">

  <section class="pass pass--textured">
    <svg class="pass__art" viewBox="0 0 390 550" xmlns="http://www.w3.org/2000/svg">
      <defs>
        <linearGradient id="sceneA" x1="0" y1="0" x2="0" y2="1">
          <stop offset="0" stop-color="var(--sky-top)"/>
          <stop offset="0.3" stop-color="var(--sky-mid)"/>
          <stop offset="0.5" stop-color="var(--hills)"/>
          <stop offset="0.7" stop-color="var(--vines)"/>
          <stop offset="1" stop-color="var(--vines-deep)"/>
        </linearGradient>
      </defs>
      <rect class="scene" x="0" y="138" width="390" height="324" fill="url(#sceneA)" role="img" aria-label="Photo: hot air balloon rising over vineyard rows at sunrise"/>
      <rect class="group-band" x="0" y="462" width="390" height="88" fill="var(--brand-blue)"/>
    </svg>
    <div class="pass__brand"><span class="pass__brand-name">Skyward</span><span class="pass__brand-sub">Ballooning</span></div>
    <h2 class="pass__title">Boarding<br>Pass</h2>
    <p class="pass__tag">#skywardballooning</p>
    <p class="pass__pilot">PILOT : MARCUS</p>
  </section>

  <section class="pass pass--clean">
    <svg class="pass__art" viewBox="0 0 390 550" xmlns="http://www.w3.org/2000/svg">
      <defs>
        <linearGradient id="sceneB" x1="0" y1="0" x2="0" y2="1">
          <stop offset="0" stop-color="var(--sky-top)"/>
          <stop offset="0.3" stop-color="var(--sky-mid)"/>
          <stop offset="0.5" stop-color="var(--hills)"/>
          <stop offset="0.7" stop-color="var(--vines)"/>
          <stop offset="1" stop-color="var(--vines-deep)"/>
        </linearGradient>
      </defs>
      <rect class="scene" x="0" y="138" width="390" height="324" fill="url(#sceneB)" role="img" aria-label="Photo: hot air balloon rising over vineyard rows at sunrise"/>
      <rect class="group-band" x="0" y="469" width="390" height="81" fill="var(--brand-blue)"/>
    </svg>
    <div class="pass__brand"><span class="pass__brand-name">Skyward</span><span class="pass__brand-sub">Ballooning</span></div>
    <h2 class="pass__title">Boarding<br>Pass</h2>
    <p class="pass__tag">#skywardballooning</p>
    <p class="pass__pilot">PILOT : MARCUS</p>
  </section>

</main>
</body>
</html>
```